依頼詳細
社名は、株式会社WUBRAN、ロゴはフリップナーの方に作成していただきました。
新しい社名、ロゴ、業務内容がイメージできるようなデザインを募集いたします。
記載項目
表面:会社ロゴ、会社名、本社住所、本社電話番号、本社FAX番号、メールアドレス、携帯番号、URL、事業部、役職、氏名

裏面:業務内容

※記載項目、増える可能性があります
希望イメージ
• +5 0 +5
• シンプル
複雑
• 単色
カラフル
• 暗い
明るい
• 日常
高級
• 遊び心
厳粛
• 未来的
伝統的
• 女性的
男性的
希望する色
納品ファイル
• 高解像度JPG (.jpg)
• イラストレーター形式 (.ai)
• フォトショップ形式 (.psd)
• PNG形式 (.png)
補足説明
提案していただいた後、決定する前に修正依頼を快く承諾してくれる方出お願いします。
修正依頼するのは、そのデザインが決定候補にあがっていると理解をお願いしたいです。
以前、修正をお願いしたら、とても嫌な言葉で返信をいただき、不快な思いをしたことがあります。
当社、30周年にあたっての、社名変更、ロゴ変更なので、慎重に決めていきたいので、ご理解をよろしくお願いいたします。
依頼公開後の追記内容
色は、金色か印刷で金色に見えるような色(黄色系)でお願いしたいです。

```html
<!DOCTYPE html>
<html lang="ja">
<head>
<meta charset="utf-8">
<title>WUBRAN 名刺デザイン</title>
<link href="https://fonts.googleapis.com/css2?family=Noto+Sans+JP:wght@400;500;700&family=Montserrat:wght@700;800&display=swap" rel="stylesheet">
<style>
  :root {
    --sheet: #ebebeb;
    --label: #555555;
    --paper: #ffffff;
    --green-deep: #0b4a24;
    --green: #11632f;
    --green-light: #1d7a3e;
    --gold: #c8a24a;
    --gold-light: #e3c777;
    --ink: #222222;
    --rule: #9a9a9a;
  }
  * { margin: 0; padding: 0; box-sizing: border-box; }
  html, body { width: 805px; height: 1200px; overflow: hidden; background: var(--sheet); }
  body { position: relative; font-family: "Noto Sans JP", sans-serif; color: var(--ink); }

  .side-label { position: absolute; left: 38px; font-size: 17px; color: var(--label); font-family: "Noto Sans JP", sans-serif; }
  .side-label--front { top: 68px; }
  .side-label--back { top: 624px; }

  .card { position: absolute; left: 38px; width: 730px; height: 451px; overflow: hidden; box-shadow: 0 2px 6px rgba(0,0,0,.18); }
  .card--front { top: 107px; background: var(--paper); }
  .card--back { top: 676px; background: linear-gradient(135deg, var(--green-light) 0%, var(--green) 45%, var(--green-deep) 100%); }

  .card__shapes { position: absolute; inset: 0; width: 100%; height: 100%; }

  .dot-field { position: absolute; left: 30px; top: 20px; width: 200px; height: 130px;
    background: radial-gradient(ellipse closest-side at 60% 50%, rgba(227,199,119,.75) 0%, rgba(200,162,74,.35) 50%, rgba(200,162,74,0) 100%); }

  .brand { position: absolute; display: flex; align-items: center; gap: 12px; color: var(--gold);
    font-family: "Montserrat", sans-serif; font-weight: 800; letter-spacing: 1px; }
  .brand__mark { border-radius: 50%; background: var(--gold); flex: none; }
  .brand--front { right: 40px; top: 48px; font-size: 44px; }
  .brand--front .brand__mark { width: 40px; height: 40px; }
  .brand--back { left: 55px; top: 175px; font-size: 46px; color: var(--gold-light); }
  .brand--back .brand__mark { width: 44px; height: 44px; background: var(--gold-light); }

  .person { position: absolute; left: 176px; top: 180px; }
  .person__role { font-size: 15px; font-weight: 500; }
  .person__name { margin-top: 4px; font-size: 34px; font-weight: 500; letter-spacing: 6px; display: flex; align-items: baseline; gap: 18px; line-height: 1.3; }
  .person__name-roman { font-size: 15px; letter-spacing: 0; font-weight: 400; }
  .person__mobile { margin-top: 2px; font-size: 17px; display: flex; align-items: center; gap: 6px; }

  .divider { position: absolute; left: 176px; top: 292px; width: 512px; height: 1px; background: var(--rule); }

  .company { position: absolute; left: 176px; top: 302px; }
  .company__name { font-size: 20px; font-weight: 500; margin-bottom: 6px; }
  .company__line { font-size: 15px; display: flex; align-items: center; gap: 8px; height: 26px; }

  .icon { width: 18px; height: 18px; flex: none; }

  .services { position: absolute; left: 360px; top: 110px; color: #ffffff; }
  .services__title { font-size: 17px; margin-bottom: 10px; }
  .services__list { list-style: none; }
  .services__item { font-size: 18px; height: 36px; display: flex; align-items: center; gap: 8px; }
  .services__item::before { content: ""; width: 12px; height: 12px; border-radius: 50%; background: #ffffff; }
</style>
</head>
<body>

  <p class="side-label side-label--front">Front</p>
  <section class="card card--front">
    <svg class="card__shapes" viewBox="0 0 730 451" aria-hidden="true">
      <path d="M0 0 H730 V14 C560 14 430 30 340 90 C270 135 180 168 0 172 Z" fill="var(--green)"/>
      <path d="M0 172 C180 168 270 135 340 90 C430 30 560 14 730 14 V22 C565 23 440 40 352 98 C280 146 185 180 0 184 Z" fill="var(--gold)"/>
    </svg>
    <div class="dot-field" role="img" aria-label="金色のハーフトーンドット装飾"></div>

    <div class="brand brand--front"><span class="brand__mark"></span>WUBRAN</div>

    <div class="person">
      <p class="person__role">電気設備事業部｜営業部長</p>
      <p class="person__name">川村 直樹<span class="person__name-roman">Naoki Kawamura</span></p>
      <p class="person__mobile">
        <svg class="icon" viewBox="0 0 18 18"><rect x="4" y="1" width="10" height="16" rx="2" fill="none" stroke="var(--green)" stroke-width="2"/><circle cx="9" cy="14" r="1.2" fill="var(--green)"/></svg>
        000-0000-0000
      </p>
    </div>

    <div class="divider"></div>

    <div class="company">
      <p class="company__name">株式会社WUBRAN</p>
      <p class="company__line">
        <svg class="icon" viewBox="0 0 18 18"><path d="M2 9 L9 2 L16 9 V16 H2 Z" fill="var(--green)"/></svg>
        〒500-0000 岐阜県緑野市若葉町 1234-5
      </p>
      <p class="company__line">
        <svg class="icon" viewBox="0 0 18 18"><rect width="18" height="18" rx="3" fill="var(--green)"/><path d="M5 4 C5 10 8 13 14 13 L14 11 L11.5 10 L10 11 C8.5 10.5 7.5 9.5 7 8 L8 6.5 L7 4 Z" fill="#fff"/></svg>
        0000-00-0000
      </p>
      <p class="company__line">
        <svg class="icon" viewBox="0 0 18 18"><rect width="18" height="18" rx="3" fill="var(--green)"/><rect x="3.5" y="5" width="11" height="8" fill="none" stroke="#fff" stroke-width="1.4"/><path d="M3.5 5 L9 10 L14.5 5" fill="none" stroke="#fff" stroke-width="1.4"/></svg>
        info@example.com
      </p>
    </div>
  </section>

  <p class="side-label side-label--back">Back</p>
  <section class="card card--back">
    <svg class="card__shapes" viewBox="0 0 730 451" aria-hidden="true">
      <path d="M260 0 C330 120 420 200 560 230 C450 170 380 100 340 0 Z" fill="rgba(255,255,255,.07)"/>
      <path d="M430 0 C470 150 560 260 730 300 V220 C610 190 520 110 500 0 Z" fill="rgba(255,255,255,.06)"/>
      <path d="M0 451 C120 360 260 330 420 380 C300 300 140 300 0 360 Z" fill="rgba(255,255,255,.05)"/>
    </svg>

    <div class="brand brand--back"><span class="brand__mark"></span>WUBRAN</div>

    <div class="services">
      <p class="services__title">【事業内容】</p>
      <ul class="services__list">
        <li class="services__item">総合省エネルギー事業</li>
        <li class="services__item">情報通信網構築事業</li>
        <li class="services__item">ファシリティ事業</li>
        <li class="services__item">ホームテクノ事業</li>
        <li class="services__item">代理店・取次店事業</li>
        <li class="services__item">環境 ECO ビジネス</li>
      </ul>
    </div>
  </section>

</body>
</html>
```